Packaging Design for High end coffee beans

The name is Cafe de Marvela.

I need this design to be amended you are welcome to design your own too.

We sell high end coffee beans from Colombia this needs to be reflected in the packaging.

The colour is black and Gold. i need the lettering to be fully gold not a fade.

It is to be printed on coffee packaging so the clarity and quality has to be ready for that.

I need Just harvest and Woodland covenant logos added.
Also to be added to the design is:
Single Origin
Traceability
Sustainability

"Awaken you senses" to be added.

I have added some jpegs that i own. you are free to use stock images where appropiate.

Target Market(s)

Coffee Consumers

Requirements
Must have
• Scalable vector files .. whatever images or file design you prodcue mut be able to be printed in high quality
High end quality
Awaken Your Senses needs tl be shown
Logos of just harvest or Wood land covenant to be added
200g weight to be shown
We have 4 beans which need to be shown individually
Velma Nectar
K3 Morandi
Teal Juniper
Altezza Amber
Nice to have
• You are welcome to come up with your own design

```html
<!DOCTYPE html>
<html lang="en">
<head>
<meta charset="utf-8">
<title>Cafe de Marvela – Teal Juniper 200g Bag</title>
<link rel="stylesheet" href="https://fonts.googleapis.com/css2?family=Barlow:wght@300;700&family=Ubuntu:wght@700&family=Oswald:wght@500&family=Open+Sans:wght@400&family=Josefin+Sans:wght@600&display=swap">
<style>
  :root {
    --backdrop: #e4b800;
    --ink: #121212;
    --black-panel: #1b1b1b;
    --gold: #d9b40a;
    --gold-light: #f2d522;
    --gold-deep: #c29a00;
    --leaf: #2f6b5a;
    --leaf-dark: #1f4a3f;
    --badge-green: #3aa070;
    --badge-blue: #2a8fd0;
  }
  * { box-sizing: border-box; margin: 0; padding: 0; }
  html, body { width: 1200px; height: 960px; overflow: hidden; }
  body { background: var(--backdrop); position: relative; }

  .bag { position: absolute; top: 40px; left: 300px; width: 610px; height: 880px; display: flex; }

  /* Side gusset */
  .side-panel { position: relative; width: 170px; height: 880px; background: var(--black-panel); overflow: hidden; }
  .side-panel__frame { position: absolute; inset: 200px 10px 30px 10px; border: 1px solid var(--gold); }
  .side-panel__title { position: absolute; top: 280px; left: 0; right: 0; text-align: center;
    font-family: "Oswald", sans-serif; font-weight: 500; font-size: 24px; color: var(--gold); }
  .side-panel__copy { position: absolute; top: 322px; left: 20px; right: 20px;
    font-family: "Open Sans", sans-serif; font-size: 7.6px; line-height: 1.4; color: var(--gold);
    text-align: justify; }
  .side-panel__copy p + p { margin-top: 9px; }
  .side-panel__sketch { position: absolute; border-radius: 40px; opacity: .5; }
  .side-panel__sketch--top { top: 210px; left: 30px; width: 110px; height: 70px;
    background: radial-gradient(ellipse at center, #3a3a3a 0%, transparent 70%); }
  .side-panel__sketch--bottom { top: 640px; left: 20px; width: 130px; height: 190px;
    background: radial-gradient(ellipse at center, #3a3a3a 0%, transparent 72%); }

  /* Front face */
  .front-panel { position: relative; width: 440px; height: 880px; overflow: hidden; }
  .front-panel__shapes { position: absolute; inset: 0; }
  .front-panel__url { position: absolute; top: 151px; left: 0; right: 0; text-align: center;
    font-family: "Barlow", sans-serif; font-weight: 700; font-size: 14px; letter-spacing: 4px; color: var(--ink); }

  .botanical { position: absolute; border-radius: 50%;
    background: radial-gradient(ellipse at 50% 50%, var(--leaf) 0%, var(--leaf-dark) 60%, rgba(31,74,63,0) 100%); }
  .botanical--top-right { top: 190px; left: 312px; width: 124px; height: 200px; }
  .botanical--left { top: 310px; left: 4px; width: 124px; height: 240px; }
  .botanical--bottom-right { top: 500px; left: 312px; width: 124px; height: 180px; }

  .brand-mark { position: absolute; top: 405px; left: 130px; width: 220px; text-align: center; color: var(--gold); }
  .brand-mark__name { display: inline-flex; align-items: center; gap: 8px; white-space: nowrap;
    font-family: "Josefin Sans", sans-serif; font-weight: 600; font-size: 16px; letter-spacing: 2px; text-transform: uppercase; }
  .brand-mark__dot { width: 10px; height: 10px; border-radius: 50%; background: var(--gold); flex: none; }
  .brand-mark__origin { margin-top: 20px; font-family: "Josefin Sans", sans-serif; font-weight: 600; font-size: 15px; letter-spacing: 1px; }
  .brand-mark__tagline { margin-top: 8px; font-family: "Josefin Sans", sans-serif; font-weight: 600; font-size: 9px; letter-spacing: 3px; text-transform: uppercase; white-space: nowrap; }
  .brand-mark__slogan { margin-top: 14px; font-family: "Josefin Sans", sans-serif; font-weight: 600; font-size: 12px; letter-spacing: 2px; text-transform: uppercase; white-space: nowrap; }

  .variety { position: absolute; left: 28px; top: 650px; color: var(--ink); font-family: "Barlow", sans-serif; }
  .variety__label { font-weight: 300; font-size: 26px; letter-spacing: 4px; line-height: 1; }
  .variety__name { font-weight: 700; font-size: 34px; letter-spacing: 5px; line-height: 1.05; text-transform: uppercase; white-space: nowrap; }

  .claims { position: absolute; left: 28px; top: 738px; list-style: none;
    font-family: "Ubuntu", sans-serif; font-weight: 700; font-size: 21px; color: var(--ink); }
  .claims li { display: flex; align-items: center; gap: 10px; height: 30px; }
  .claims svg { width: 16px; height: 16px; }

  .cert-badge { position: absolute; left: 370px; width: 50px; height: 50px; border-radius: 50%; }
  .cert-badge--woodland { top: 705px; background: var(--badge-green); }
  .cert-badge--harvest { top: 772px; background: var(--ink); border: 4px solid var(--badge-blue); }

  .net-weight { position: absolute; left: 190px; top: 838px; font-family: "Barlow", sans-serif; font-weight: 700; color: var(--ink); line-height: 1; }
  .net-weight__label { font-size: 10px; letter-spacing: 1px; margin-right: 6px; }
  .net-weight__value { font-size: 24px; }
</style>
</head>
<body>
  <div class="bag">
    <section class="side-panel">
      <div class="side-panel__sketch side-panel__sketch--top" role="img" aria-label="Line sketch of coffee leaves"></div>
      <div class="side-panel__frame"></div>
      <h2 class="side-panel__title">About Us</h2>
      <div class="side-panel__copy">
        <p>We specialise in importing high end specialty Colombian coffee beans. Our beans are sourced directly from Colombian farmers who have generations of coffee growing experience. Colombian coffee carries a unique love from the families who cultivate it, and it is this care that gives the product its extra quality. As part of this family we produce coffee ethically under just harvest policies.</p>
        <p>We have offices in Colombia and China. Our aim is to grow and bring our coffee across the globe, one continent at a time.</p>
        <p>Buying our own farm (finca) is a key part of our global goal, giving us a steady supply of beans.</p>
      </div>
      <div class="side-panel__sketch side-panel__sketch--bottom" role="img" aria-label="Faint line sketch of coffee branches and cherries"></div>
    </section>

    <section class="front-panel">
      <svg class="front-panel__shapes" viewBox="0 0 440 880" width="440" height="880">
        <defs>
          <linearGradient id="goldFoil" x1="0" y1="0" x2="1" y2="1">
            <stop offset="0" stop-color="#c29a00"/>
            <stop offset=".5" stop-color="#d9b40a"/>
            <stop offset="1" stop-color="#f2d522"/>
          </linearGradient>
        </defs>
        <rect class="seal" x="0" y="0" width="440" height="120" fill="#121212"/>
        <rect class="label-field" x="0" y="120" width="440" height="760" fill="url(#goldFoil)"/>
        <path class="black-wave" d="M0,205 C140,195 280,250 440,232 L440,640 C330,600 220,640 120,625 C70,618 30,615 0,620 Z" fill="#1b1b1b"/>
        <circle class="valve" cx="215" cy="290" r="28" fill="none" stroke="#2c2c2c" stroke-width="3"/>
        <circle cx="215" cy="290" r="2" fill="#2c2c2c"/>
      </svg>

      <p class="front-panel__url">www.marvelacafe.com</p>

      <div class="botanical botanical--top-right" role="img" aria-label="Illustrated coffee branch with green leaves, white blossoms and red cherries"></div>
      <div class="botanical botanical--left" role="img" aria-label="Illustrated coffee branch with green leaves, white blossoms and red cherries"></div>
      <div class="botanical botanical--bottom-right" role="img" aria-label="Illustrated coffee branch with green leaves, white blossoms and red cherries"></div>

      <div class="brand-mark">
        <div class="brand-mark__name"><span class="brand-mark__dot"></span>Cafe de Marvela</div>
        <p class="brand-mark__origin">100% COLOMBIANO</p>
        <p class="brand-mark__tagline">Specialty Coffee Beans</p>
        <p class="brand-mark__slogan">Awaken Your Senses</p>
      </div>

      <div class="variety">
        <p class="variety__label">TYPE</p>
        <h1 class="variety__name">Teal Juniper</h1>
      </div>

      <ul class="claims">
        <li><svg viewBox="0 0 16 16"><path d="M2 8.5 L6 12.5 L14 3.5" fill="none" stroke="#121212" stroke-width="2.6"/></svg>Single Origin</li>
        <li><svg viewBox="0 0 16 16"><path d="M2 8.5 L6 12.5 L14 3.5" fill="none" stroke="#121212" stroke-width="2.6"/></svg>Traceability</li>
        <li><svg viewBox="0 0 16 16"><path d="M2 8.5 L6 12.5 L14 3.5" fill="none" stroke="#121212" stroke-width="2.6"/></svg>Sustainability</li>
      </ul>

      <div class="cert-badge cert-badge--woodland" role="img" aria-label="Woodland covenant certification badge"></div>
      <div class="cert-badge cert-badge--harvest" role="img" aria-label="Just harvest certification badge"></div>

      <p class="net-weight"><span class="net-weight__label">NET WT.</span><span class="net-weight__value">200g</span></p>
    </section>
  </div>
</body>
</html>
```